Web design for sitter site

We will be launching a sitter site in the coming months that focuses on sitters for children. The name of this site will be KidHaven.com
We will need:
1. main page design
2. site logo designed
3. subpages as well for the look of people's profiles, and job listings, etc (see links below)
We only need the design, photos, font files, etc. We do not need this site coded (no html), a ps job is fine.
Some competing sites in the space include - tendlyhub.com and vurl.com
http://www.brisk-minder.example/images/profile1.jpg
http://quenthollibrary.example/wp-content/uploads/2013/09/vurl-review.png
http://www.palvermont.example/hr/photos/tendly_hub2.jpg
Target Market(s)
Mothers of children, mainly women
Industry/Entity Type
Online
Look and feel

```html
<!DOCTYPE html>
<html lang="en">
<head>
<meta charset="utf-8">
<title>KidHaven.com — Baby Sitter Services</title>
<link rel="stylesheet" href="https://fonts.googleapis.com/css2?family=Cinzel:wght@400;600;700&family=Source+Sans+3:wght@400;600&family=Arimo:wght@400&display=swap">
<style>
  :root {
    --purple: #72006f;
    --sky: #d6eaf6;
    --gold: #c9962a;
    --ink: #3a3a3a;
    --ink-soft: #4a4a4a;
    --footer-dark: #1b1b1b;
    --link-light: #d9c6d8;
    --white: #ffffff;
  }
  * { box-sizing: border-box; margin: 0; padding: 0; }
  html, body { width: 1063px; height: 1200px; overflow: hidden; background: var(--white); }
  body { position: relative; font-family: "Source Sans 3", "Myriad Pro", sans-serif; color: var(--ink); }

  .top-rule { position: absolute; left: 0; top: 0; width: 1063px; height: 8px; background: var(--purple); }

  .brand {
    position: absolute; left: 92px; top: 44px;
    font-family: "Source Sans 3", sans-serif; font-weight: 600;
    font-size: 42px; line-height: 50px; color: var(--purple); letter-spacing: -0.5px;
  }

  .main-nav {
    position: absolute; left: 70px; top: 120px; width: 925px; height: 43px;
    background: var(--purple);
  }
  .main-nav a {
    position: absolute; top: 0; line-height: 43px;
    color: var(--white); text-decoration: none; font-size: 17px; font-weight: 400;
    text-transform: uppercase;
  }

  .hero-title {
    position: absolute; left: 93px; top: 196px;
    font-family: "Cinzel", serif; font-weight: 400; font-size: 40px; line-height: 48px;
    color: var(--purple);
  }
  .hero-rule { position: absolute; left: 105px; top: 252px; width: 454px; height: 1px; background: var(--gold); }
  .hero-copy {
    position: absolute; left: 92px; top: 268px; width: 430px;
    font-size: 16px; line-height: 20.2px; color: var(--ink);
  }
  .btn {
    position: absolute; background: var(--sky); border-radius: 4px;
    color: #222; text-align: center; text-decoration: none;
  }
  .btn-learn { left: 92px; top: 380px; width: 137px; height: 44px; line-height: 44px; font-size: 18px; text-transform: uppercase; }

  .hero-photo {
    position: absolute; left: 558px; top: 194px; width: 451px; height: 340px;
    border-radius: 160px 60px 0 0;
    background: linear-gradient(110deg, #8a5a34 0%, #c99a72 35%, #9b7c5e 60%, #d9a9a6 100%);
  }

  .hero-band { position: absolute; left: 0; top: 534px; width: 1063px; height: 50px; background: var(--sky); }
  .hero-band-rule { position: absolute; left: 0; top: 584px; width: 1063px; height: 6px; background: var(--purple); }

  .slider-dots { position: absolute; top: 601px; left: 0; width: 1063px; height: 16px; }
  .slider-dots span { position: absolute; top: 0; width: 15px; height: 15px; border-radius: 50%; background: #959595; }
  .slider-dots span.is-active { background: var(--purple); }

  .feature { position: absolute; top: 660px; width: 250px; }
  .feature-title {
    text-align: center; font-family: "Cinzel", serif; font-weight: 600;
    font-size: 27px; line-height: 32px; color: var(--purple);
  }
  .feature-sub {
    text-align: center; font-family: "Cinzel", serif; font-weight: 700;
    font-size: 14px; letter-spacing: 8px; color: var(--purple); margin-top: 2px; padding-left: 8px;
  }
  .feature-copy {
    position: absolute; top: 89px; font-family: "Arimo", Arial, sans-serif;
    font-size: 15px; line-height: 18px; color: var(--ink-soft); width: 240px;
  }
  .feature-divider {
    position: absolute; top: 674px; width: 2px; height: 262px;
    background: linear-gradient(to bottom, rgba(201,150,42,0) 0%, var(--gold) 20%, var(--gold) 80%, rgba(201,150,42,0) 100%);
  }
  .btn-read { width: 107px; height: 35px; line-height: 35px; font-size: 17px; top: 886px; color: #333; }

  .site-footer { position: absolute; left: 0; top: 957px; width: 1063px; height: 154px; background: var(--purple); }
  .footer-col { position: absolute; top: 38px; }
  .footer-col h4 {
    font-family: "Cinzel", serif; font-weight: 600; font-size: 16px; letter-spacing: 0.5px;
    color: var(--white); line-height: 20px; margin-bottom: 12px;
  }
  .footer-col a {
    display: block; font-family: "Arimo", Arial, sans-serif; font-size: 13px; line-height: 25px;
    color: var(--link-light); text-decoration: none;
  }

  .footer-bar { position: absolute; left: 0; top: 1111px; width: 1063px; height: 89px; background: var(--footer-dark); }
  .footer-brand {
    position: absolute; left: 105px; top: 27px;
    font-family: "Source Sans 3", sans-serif; font-weight: 600; font-size: 32px; line-height: 38px; color: #8d8d8d;
  }
  .social { position: absolute; top: 33px; width: 28px; height: 28px; background: var(--sky); border-radius: 2px; }
</style>
</head>
<body>
  <div class="top-rule"></div>

  <header>
    <div class="brand">KidHaven.com</div>
    <nav class="main-nav">
      <a href="#" style="left:54px">Home</a>
      <a href="#" style="left:145px">About</a>
      <a href="#" style="left:234px">Sitters</a>
      <a href="#" style="left:333px">FAQ</a>
      <a href="#" style="left:391px">Testimonials</a>
      <a href="#" style="left:539px">Sitter Search</a>
      <a href="#" style="left:682px">Resources</a>
      <a href="#" style="left:801px">Contact</a>
    </nav>
  </header>

  <section class="hero">
    <h1 class="hero-title">Baby Sitter Services</h1>
    <div class="hero-rule"></div>
    <p class="hero-copy">Lorem ipsum dolor sit amet consectetur adipiscing elit und lorem&nbsp; sit amet consectetur adipiscing elit lorem ipsum dolor sit amet consectetur&nbsp; elit lorem ipsum dolor<br>sit amet&nbsp; adipiscing elit.</p>
    <a class="btn btn-learn" href="#">Learn More</a>
    <div class="hero-photo" role="img" aria-label="Photo of a smiling young sitter holding a little girl wearing a tiara"></div>
    <div class="hero-band"></div>
    <div class="hero-band-rule"></div>
    <div class="slider-dots">
      <span class="is-active" style="left:428px"></span>
      <span style="left:475px"></span>
      <span style="left:521px"></span>
      <span style="left:568px"></span>
      <span style="left:615px"></span>
    </div>
  </section>

  <section class="features">
    <article class="feature" style="left:99px">
      <h2 class="feature-title">Hiring</h2>
      <div class="feature-sub">Staff</div>
      <p class="feature-copy" style="left:9px">Lorem ipsum dolor sit amet et aeu consectetur adipiscing elit. Lorem ipsum dolor sit amet consectetur adipiscing elit et loraer sit.<br>Lorem ipsum dolor sitamet et aeu consectetur adipiscing elit sit.</p>
    </article>
    <div class="feature-divider" style="left:377px"></div>
    <article class="feature" style="left:407px">
      <h2 class="feature-title">Sitter</h2>
      <div class="feature-sub">Services</div>
      <p class="feature-copy" style="left:11px">Lorem ipsum dolor sit amet et aeu consectetur adipiscing elit. Lorem ipsum dolor sit amet consectetur adipiscing elit et loraer sit.<br>Lorem ipsum dolor sitamet et aeu consectetur adipiscing elit sit.</p>
    </article>
    <div class="feature-divider" style="left:686px"></div>
    <article class="feature" style="left:718px">
      <h2 class="feature-title">Something</h2>
      <div class="feature-sub">Here&nbsp; Too</div>
      <p class="feature-copy" style="left:11px">Lorem ipsum dolor sit amet et aeu consectetur adipiscing elit. Lorem ipsum dolor sit amet consectetur adipiscing elit et loraer sit.<br>Lorem ipsum dolor sitamet et aeu consectetur adipiscing elit sit.</p>
    </article>
    <a class="btn btn-read" href="#" style="left:170px">Read more</a>
    <a class="btn btn-read" href="#" style="left:479px">Read more</a>
    <a class="btn btn-read" href="#" style="left:787px">Read more</a>
  </section>

  <footer>
    <div class="site-footer">
      <div class="footer-col" style="left:122px"><h4>Interesting Links</h4><a href="#">link one goes here</a><a href="#">link two goes here</a></div>
      <div class="footer-col" style="left:347px"><h4>Sitter Services</h4><a href="#">link one goes here</a><a href="#">link one goes here</a></div>
      <div class="footer-col" style="left:571px"><h4>Something</h4><a href="#">link one goes here</a><a href="#">link two goes here</a></div>
      <div class="footer-col" style="left:804px"><h4>Contact</h4><a href="#">link one goes here</a><a href="#">link two goes here</a></div>
    </div>
    <div class="footer-bar">
      <div class="footer-brand">KidHaven.com</div>
      <a class="social" href="#" style="left:870px" aria-label="Social profile one"></a>
      <a class="social" href="#" style="left:909px" aria-label="Social profile two"></a>
      <a class="social" href="#" style="left:948px" aria-label="Social profile three"></a>
    </div>
  </footer>
</body>
</html>
```